Fleet Wrap - Wall Partitions Company

We are looking for a vehicle/fleet wrap design for Brightfold Panel Works, a company that sells and installs operable/folding wall partitions for commercial spaces. Our systems are used in offices, schools, hotels, conference centers, and other spaces that need flexible room configurations.

The goal of the wrap is to improve brand visibility and recognition while our vehicles are on the road and at job sites. We want the design to feel modern, professional, architectural, and memorable, while making it immediately clear what our company does.

The design should incorporate imagery, graphics, or architectural elements that communicate movable walls, folding partitions, and/or flexible spaces, along with our company colors (see logo attached). As well as display our logo/name, location, and phone number (obtained from our website - brightfoldpanels.example). We are open to creative concepts, but would prefer something clean and distinctive rather than overly busy.

The vehicle we want wrapped, is a KESTA Voyant 2400 (see link here - https://www.kestavans.example/kesta-voyant/specs.2400-cargo-van-high-roof-159-wb.html)

Key priorities:
- Strong brand visibility from a distance
- Contemporary, architectural look
- Clearly communicate that we sell and install folding/operable wall systems
- Easy-to-read company name and website
- Professional enough for commercial construction and corporate clients

```html
<!DOCTYPE html>
<html lang="en">
<head>
<meta charset="utf-8">
<title>Brightfold Panel Works – Fleet Wrap</title>
<link href="https://fonts.googleapis.com/css2?family=Poppins:wght@500;600;700&display=swap" rel="stylesheet">
<style>
  :root{
    --bg:#ececec;
    --van-white:#f4f4f4;
    --van-line:#c9c9c9;
    --trim:#2b2b2b;
    --glass:#5a5d61;
    --brand-blue:#1f6fd1;
    --brand-blue-deep:#2a6bb3;
    --brand-orange:#e8820c;
    --ink:#262626;
    --tire:#1c1c1c;
    --hub:#b9bcc0;
  }
  html,body{margin:0;padding:0;overflow:hidden;background:var(--bg);}
  .canvas{width:1200px;height:1200px;position:relative;background:var(--bg);}
  .fleet-art{display:block;width:1200px;height:1200px;}
  .body-shell{fill:var(--van-white);stroke:var(--van-line);stroke-width:1.5;}
  .panel-seam{stroke:var(--van-line);stroke-width:1.5;fill:none;}
  .bumper{fill:var(--trim);}
  .cab-glass{fill:var(--glass);}
  .tire{fill:var(--tire);}
  .hub{fill:var(--hub);stroke:#8e9196;stroke-width:2;}
  .stripe-blue{fill:var(--brand-blue);}
  .field-blue{fill:var(--brand-blue-deep);}
  .band-orange{fill:var(--brand-orange);}
  .shadow{fill:#000;opacity:.18;}
  .brand-name{font-family:"Poppins",sans-serif;font-weight:600;fill:var(--ink);letter-spacing:.5px;}
  .brand-mark{fill:var(--brand-orange);}
  .phone{font-family:"Poppins",sans-serif;font-weight:700;fill:#fff;}
  .web{font-family:"Poppins",sans-serif;font-weight:600;}
  .web-blue{fill:var(--brand-blue);}
  .web-dark{fill:var(--ink);}
  .address{font-family:"Poppins",sans-serif;font-weight:500;fill:var(--ink);}
</style>
</head>
<body>
<main class="canvas">
<svg class="fleet-art" viewBox="0 0 960 960" xmlns="http://www.w3.org/2000/svg">
  <defs>
    <linearGradient id="partitionPhoto" x1="0" y1="0" x2="0" y2="1">
      <stop offset="0" stop-color="#cdb9a0"/>
      <stop offset=".45" stop-color="#e6ddd2"/>
      <stop offset=".8" stop-color="#c7d4e4"/>
      <stop offset="1" stop-color="#2a6bb3"/>
    </linearGradient>
    <clipPath id="vanTopClip">
      <path d="M72,102 Q72,88 92,88 L600,88 Q650,90 700,118 L795,212 Q850,236 885,252 Q905,264 905,292 L905,385 L72,385 Z"/>
    </clipPath>
    <clipPath id="vanBottomClip">
      <path d="M76,545 Q76,530 96,530 L605,530 Q655,532 705,560 L800,655 Q855,678 888,694 Q908,706 908,734 L908,828 L76,828 Z"/>
    </clipPath>
  </defs>

  <!-- ===== Van, curb side ===== -->
  <g class="van van--upper">
    <ellipse class="shadow" cx="490" cy="438" rx="420" ry="10"/>
    <path class="body-shell" d="M72,102 Q72,88 92,88 L600,88 Q650,90 700,118 L795,212 Q850,236 885,252 Q905,264 905,292 L905,385 L72,385 Z"/>
    <g clip-path="url(#vanTopClip)">
      <rect x="72" y="88" width="250" height="300" fill="url(#partitionPhoto)" role="img" aria-label="Photo of folding wall partitions in an office interior"/>
      <polygon class="field-blue" points="72,300 300,230 345,385 72,385"/>
      <polygon class="stripe-blue" points="236,88 250,88 300,232 287,232"/>
      <polygon class="band-orange" points="300,296 700,296 700,385 330,385"/>
      <rect class="bumper" x="72" y="330" width="110" height="60"/>
      <rect class="bumper" x="840" y="300" width="70" height="90"/>
      <rect class="bumper" x="270" y="343" width="440" height="20"/>
    </g>
    <path class="panel-seam" d="M400,100 L400,382 M595,100 L595,382 M610,150 L700,150 L770,236 L770,382"/>
    <path class="cab-glass" d="M622,160 L690,160 L760,240 L760,262 L622,262 Z"/>
    <rect class="bumper" x="565" y="258" width="14" height="26" rx="4"/>
    <rect class="bumper" x="620" y="258" width="14" height="26" rx="4"/>
    <rect class="bumper" x="190" y="236" width="205" height="8" rx="3"/>

    <rect class="brand-mark" x="392" y="130" width="22" height="22"/>
    <text class="brand-name" x="424" y="150" font-size="24">BRIGHTFOLD</text>
    <text class="brand-name" x="424" y="178" font-size="24">PANEL WORKS</text>

    <text class="web web-blue" x="332" y="276" font-size="14">www.brightfoldpanels.example</text>
    <text class="phone" x="333" y="334" font-size="29">201-555-0186</text>
    <text class="address" x="646" y="280" font-size="9">48 Alder Way</text>
    <text class="address" x="646" y="293" font-size="9">Hollis Ridge NJ 07400</text>

    <circle class="tire" cx="210" cy="392" r="48"/>
    <circle class="hub" cx="210" cy="392" r="26"/>
    <circle class="tire" cx="775" cy="392" r="48"/>
    <circle class="hub" cx="775" cy="392" r="26"/>
  </g>

  <!-- ===== Van, road side ===== -->
  <g class="van van--lower">
    <ellipse class="shadow" cx="492" cy="880" rx="420" ry="10"/>
    <path class="body-shell" d="M76,545 Q76,530 96,530 L605,530 Q655,532 705,560 L800,655 Q855,678 888,694 Q908,706 908,734 L908,828 L76,828 Z"/>
    <g clip-path="url(#vanBottomClip)">
      <path class="stripe-blue" d="M76,680 L470,680 Q590,684 640,760 L695,832 L650,832 L600,770 Q560,705 460,700 L76,700 Z"/>
      <path class="band-orange" d="M76,688 L460,688 Q575,692 615,760 L665,832 L76,832 Z"/>
      <rect class="bumper" x="76" y="770" width="115" height="60"/>
      <rect class="bumper" x="845" y="745" width="70" height="90"/>
      <rect class="bumper" x="270" y="786" width="440" height="20"/>
    </g>
    <path class="panel-seam" d="M405,545 L405,825 M605,545 L605,825 M615,595 L705,595 L775,680 L775,825"/>
    <path class="cab-glass" d="M627,603 L695,603 L765,683 L765,705 L627,705 Z"/>
    <rect class="bumper" x="570" y="700" width="14" height="26" rx="4"/>
    <rect class="bumper" x="625" y="700" width="14" height="26" rx="4"/>
    <rect class="bumper" x="195" y="676" width="205" height="8" rx="3"/>

    <rect class="brand-mark" x="118" y="592" width="30" height="30"/>
    <text class="brand-name" x="160" y="618" font-size="32">BRIGHTFOLD PANEL WORKS</text>

    <text class="phone" x="140" y="720" font-size="26">201-555-0186</text>
    <text class="web web-dark" x="140" y="738" font-size="13">www.brightfoldpanels.example</text>
    <text class="address" x="432" y="760" font-size="11">48 Alder Way</text>
    <text class="address" x="432" y="776" font-size="11">Hollis Ridge NJ 07400</text>

    <circle class="tire" cx="212" cy="832" r="48"/>
    <circle class="hub" cx="212" cy="832" r="26"/>
    <circle class="tire" cx="778" cy="832" r="48"/>
    <circle class="hub" cx="778" cy="832" r="26"/>
  </g>
</svg>
</main>
</body>
</html>
```